New Business Card & Logo Design Project for PR Agency

Halvery & Partners Tech Public Relations agency is looking for a new business card design. Please see our website at www.halvery-pr.example for a description of our services. The design does not necessarily have to match the website’s aesthetic as we are looking for something fresh and modern that reflects our business. We want to emphasize that our focus is on media & public relations, content creation, social media and SEO. We want the business card to convey our BtoB technology focus and should have a very clean look. You are welcome to draw from our current halvery & partners logo on the card or play with that design too. We also like the idea of utilizing blue and white, which are often used in technology-related designs and layouts.
Attached are jpegs of the current logo and current card design for your reference.
Target Market(s)
Our clients are Business-to-Business technology providers.We sell our services to the CEO/President/Marketing director of a technology providing company.
Industry/Entity Type
Business
Look and feel

```html
<!DOCTYPE html>
<html lang="en">
<head>
<meta charset="utf-8">
<title>Halvery &amp; Partners – Business Card</title>
<link rel="stylesheet" href="https://fonts.googleapis.com/css2?family=Montserrat+Alternates:wght@500;600&display=swap">
<style>
  :root {
    --stage: #e9eaee;
    --card: #ffffff;
    --navy: #2440a8;
    --cyan: #22c9ec;
    --magenta: #e8155a;
    --shadow: rgba(20, 24, 50, 0.18);
  }
  * { box-sizing: border-box; margin: 0; padding: 0; }
  html, body { width: 1200px; height: 800px; overflow: hidden; }
  body {
    background: var(--stage);
    font-family: "Montserrat Alternates", "Helvetica Neue", Arial, sans-serif;
    color: var(--navy);
    position: relative;
  }
  .card {
    position: absolute;
    top: 252px;
    width: 520px;
    height: 297px;
    background: var(--card);
    box-shadow: 0 10px 30px var(--shadow);
    overflow: hidden;
  }
  .card--front { left: 50px; }
  .card--back { left: 630px; }

  /* front */
  .brand {
    display: flex;
    align-items: center;
    gap: 12px;
    font-weight: 600;
    color: var(--navy);
  }
  .brand__square {
    width: 22px; height: 22px;
    background: var(--cyan);
    flex: none;
  }
  .card--front .brand {
    position: absolute;
    left: 0; right: 0; top: 110px;
    justify-content: center;
    font-size: 32px;
  }
  .tagline {
    position: absolute;
    right: 0; bottom: 26px;
    width: 200px;
    padding: 10px 18px;
    background: var(--magenta);
    color: #fff;
    font-size: 17px;
    font-weight: 500;
    line-height: 1.05;
    text-align: right;
  }

  /* back */
  .card--back .brand {
    position: absolute;
    left: 30px; top: 34px;
    font-size: 24px;
  }
  .divider {
    position: absolute;
    left: 0; right: 0; top: 92px;
    height: 1.5px;
    background: var(--navy);
  }
  .address {
    position: absolute;
    left: 30px; top: 112px;
    font-size: 12px;
    font-weight: 600;
    line-height: 1.35;
    font-style: normal;
  }
  .person {
    position: absolute;
    right: 30px; top: 112px;
    text-align: right;
    color: var(--cyan);
    font-weight: 500;
  }
  .person__name { font-size: 16px; letter-spacing: 0.5px; }
  .person__role { font-size: 15px; }
  .contacts {
    position: absolute;
    right: 30px; bottom: 34px;
    list-style: none;
    font-size: 13px;
    font-weight: 600;
    line-height: 1.8;
  }
  .contacts__label {
    display: inline-block;
    width: 24px;
    color: var(--cyan);
    font-weight: 500;
  }
</style>
</head>
<body>
  <section class="card card--front" aria-label="Card front">
    <div class="brand"><span class="brand__square"></span>halvery &amp; partners</div>
    <p class="tagline">a public<br>relations company</p>
  </section>

  <section class="card card--back" aria-label="Card back">
    <div class="brand"><span class="brand__square"></span>halvery &amp; partners</div>
    <div class="divider"></div>
    <address class="address">
      48,Linden Avenue,<br>Suite 2,<br>Fairhaven,<br>Vermont,<br>05743
    </address>
    <div class="person">
      <p class="person__name">DANIEL REEVE</p>
      <p class="person__role">Partner</p>
    </div>
    <ul class="contacts">
      <li><span class="contacts__label">e</span>dreeve@halvery-pr.example</li>
      <li><span class="contacts__label">w</span>www.halvery-pr.example</li>
      <li><span class="contacts__label">f</span>802 555 014</li>
    </ul>
  </section>
</body>
</html>
```